Sell the dream! Property investment proposal document

We are looking for a proposal document which outlines our vision for property development. The purpose of the document is to raise investment from investors - sell the dream!
Brief summary:
Tarrow Dwellings Developments, is an emerging New Zealand property investment company with a focus on providing unique property investment opportunities.
Our expertise and capabilities in architectural modular homes provide us with a remarkable advantage in tackling the development of properties that are typically considered challenging, remote, or uniquely positioned.
Our specialization in this niche sector of property development not only sets us apart from competitors, but also paves the way for lucrative investment opportunities in the New Zealand property market.
Feel free to use any images from www.tarrowdwellings.co.nz
Target Market(s)
investors for a unique property development opportunity
Industry/Entity Type
luxury property development in unique locations throughout New Zealand
Font styles to use
Colors
Designer to choose only greyscale colors for use in the design.
Look and feel

```html
<!DOCTYPE html>
<html lang="en">
<head>
<meta charset="utf-8">
<title>Tarrow Dwellings – Investment Proposal</title>
<link href="https://fonts.googleapis.com/css2?family=Questrial&family=Roboto:wght@300;400&display=swap" rel="stylesheet">
<style>
  :root{
    --backdrop:#d8d8d8;
    --paper:#ffffff;
    --charcoal:#2e2b2c;
    --ink-black:#060606;
    --ink:#2a2a2a;
    --body:#3c3c3c;
    --white:#ffffff;
  }
  *{box-sizing:border-box;margin:0;padding:0}
  html,body{width:1200px;height:575px;overflow:hidden;background:var(--backdrop)}
  .spread{position:relative;width:1200px;height:575px}
  .page{position:absolute;top:36px;width:352px;height:498px;background:var(--paper);
        box-shadow:0 4px 14px rgba(0,0,0,.25);overflow:hidden}
  .page--cover{left:35px;background:var(--charcoal)}
  .page--overview{left:420px}
  .page--summary{left:806px}
  .cover-art{position:absolute;inset:0}
  .brand-name{position:absolute;left:49px;top:50px;font-family:"Questrial",sans-serif;
        font-size:30px;color:var(--white);letter-spacing:-.5px}
  .cover-title{position:absolute;left:24px;top:320px;font-family:"Questrial",sans-serif;
        font-size:20px;line-height:26.5px;color:var(--white)}
  .contact{position:absolute;right:40px;display:flex;align-items:center;gap:6px;
        font-family:"Questrial",sans-serif;font-size:9px;color:var(--white)}
  .contact--phone{top:414px}
  .contact--email{top:443px}
  .contact-icon{width:24px;height:24px;border-radius:50%;background:var(--white);
        border:2px solid var(--ink-black);box-shadow:0 0 0 1.5px var(--white);
        display:flex;align-items:center;justify-content:center}
  .section-title{position:absolute;font-family:"Questrial",sans-serif;font-size:14px;
        color:var(--ink);letter-spacing:.2px;white-space:nowrap}
  .copy{position:absolute;font-family:"Roboto",sans-serif;font-weight:300;color:var(--body);
        text-align:justify}
  .copy p{margin-bottom:7.9px}
  .copy--small{font-size:6.3px;line-height:7.9px}
  .copy--medium{font-size:6.6px;line-height:9.3px}
  .copy--medium p{margin-bottom:9.3px}
  .photo{position:absolute}
  .origins-label{position:absolute;left:101px;top:314px;width:149px;height:24px;background:var(--paper);
        display:flex;align-items:center;justify-content:center}
  .origins-label .section-title{position:static}
</style>
</head>
<body>
<main class="spread">

  <section class="page page--cover">
    <svg class="cover-art" width="352" height="498" viewBox="0 0 352 498">
      <defs>
        <linearGradient id="interiorTone" x1="0" y1="0" x2="1" y2="1">
          <stop offset="0" stop-color="#a89a80"/>
          <stop offset=".5" stop-color="#6d6458"/>
          <stop offset="1" stop-color="#9a9894"/>
        </linearGradient>
      </defs>
      <polygon role="img" aria-label="Interior photo of a leather lounge chair beside tall windows facing a grassy hillside" points="0,188 352,16 352,302 263,346 0,215" fill="url(#interiorTone)"/>
      <polygon class="cover-band" points="0,215 263,346 245,355 0,236" fill="var(--white)"/>
      <polygon class="cover-wedge" points="0,236 245,355 0,478" fill="var(--ink-black)"/>
    </svg>
    <div class="brand-name">Tarrow</div>
    <h1 class="cover-title" style="font-weight:400">MODULAR<br>ARCHITECTURAL<br>HOMES</h1>
    <div class="contact contact--phone">09 555 0142
      <span class="contact-icon"><svg width="9" height="9" viewBox="0 0 24 24"><path d="M6.6 10.8a15.1 15.1 0 0 0 6.6 6.6l2.2-2.2a1 1 0 0 1 1-.25 11.4 11.4 0 0 0 3.6.57 1 1 0 0 1 1 1V20a1 1 0 0 1-1 1A17 17 0 0 1 3 4a1 1 0 0 1 1-1h3.5a1 1 0 0 1 1 1c0 1.25.2 2.45.57 3.57a1 1 0 0 1-.25 1z" fill="#000"/></svg></span>
    </div>
    <div class="contact contact--email">sales@tarrowdwellings.co.nz
      <span class="contact-icon"><svg width="9" height="9" viewBox="0 0 24 24"><rect x="2" y="5" width="20" height="14" rx="2" fill="#000"/><path d="M2.5 6l9.5 7 9.5-7" stroke="#fff" stroke-width="1.6" fill="none"/></svg></span>
    </div>
  </section>

  <section class="page page--overview">
    <h2 class="section-title" style="left:24px;top:17px;font-weight:400">BUSINESS OVERVIEW</h2>
    <div class="photo" role="img" aria-label="Photo of a glass-walled modular home on a coastal point at sunset" style="left:204px;top:20px;width:119px;height:124px;background:linear-gradient(180deg,#b3b8bd 0%,#d9c4a0 45%,#6c6c6a 70%,#8a867f 100%)"></div>
    <div class="copy copy--small" style="left:25px;top:43px;width:168px">
      <p>Tarrow Dwellings Developments, is an emerging New Zealand property investment company with a focus on providing unique property investment opportunities.</p>
      <p>Our expertise and capabilities in architectural modular homes provide us with a remarkable advantage in tackling the development of properties that are typically considered challenging, remote, or uniquely positioned.</p>
      <p>As a company, with 48 employees boasting a wealth of experience in handling complex architectural projects, making us well-equipped to navigate the intricacies and demands of such ventures.</p>
    </div>
    <div class="copy copy--small" style="left:25px;top:153px;width:300px">
      <p>This advantage allows us to not only execute projects efficiently but also to deliver exceptional results within condensed time frames.</p>
      <p>By capitalizing on our ability to develop difficult, remote, or one-of-a-kind properties swiftly and effectively, Tarrow Dwellings Developments offers investors a rare chance to engage in projects that promise exceptional profitability in the New Zealand property market.</p>
      <p>Our specialization in this niche sector of property development not only sets us apart from competitors, but also paves the way for lucrative investment opportunities in the New Zealand property market.</p>
    </div>
    <div class="photo" role="img" aria-label="Photo of lounge chairs in a dark interior looking out over the sea" style="left:25px;top:238px;width:300px;height:87px;background:linear-gradient(180deg,#7d9bc0 0%,#4f6e95 45%,#222 75%,#3a2a22 100%)"></div>
    <div class="origins-label"><h2 class="section-title" style="font-weight:400">BUSINESS ORIGINS</h2></div>
    <div class="copy copy--small" style="left:25px;top:345px;width:300px">
      <p>Tarrow Dwellings Developments was established with the goal of transforming the property investment market in New Zealand by introducing an innovative approach that centers on architectural modular designs and streamlined project timelines.</p>
      <p>Driven by our enthusiasm for architecture and real estate, we have expanded our successful business model to not only offer financial opportunities for investors but also to expand on our passion for high-end architectural design.</p>
      <p>With a wealth of experience accumulated over the past six years in the construction and the property market, we are pivoting to focus solely on our property development initiatives, presenting completed Tarrow projects to the market, in exclusive locations. These projects will boast high-quality standards, meticulous attention to detail and landscaping, and creative design elements.</p>
      <p>By introducing completed Tarrow properties into the market, we aim to reach a wider audience, catering to individuals who prefer ready-to-occupy homes, over engaging in the design and construction process. This approach also simplifies the financing process for prospective buyers, as established properties are often preferred by financial lenders.</p>
    </div>
  </section>

  <section class="page page--summary">
    <div class="photo" role="img" aria-label="Aerial photo of a long low modular home on green coastal farmland at dusk" style="left:24px;top:19px;width:300px;height:87px;background:linear-gradient(180deg,#8a8a6e 0%,#5b5a2f 35%,#3a3322 60%,#6b6a33 100%)"></div>
    <h2 class="section-title" style="left:24px;top:118px;font-weight:400">COMPETITIVE ADVANTAGE</h2>
    <div class="copy copy--medium" style="left:24px;top:139px;width:300px">
      <p>Our competitive advantage lies in the uniqueness of our property investment opportunities. Unlike traditional real estate companies, we focus on offering properties that are not only profitable but also aesthetically pleasing and unique. By catering to the tastes of architecture lovers, we set ourselves apart from the competition and attract a niche market of customers who appreciate the artistry and design of our projects.</p>
      <p>Additionally, the streamlined and condensed timelines facilitated by our modular approach provide quicker returns on investment.</p>
    </div>
    <h2 class="section-title" style="left:24px;top:227px;font-weight:400">FINANCIAL SUMMARY</h2>
    <div class="copy copy--medium" style="left:25px;top:251px;width:300px">
      <p>In terms of financial projections, with each development, we anticipate a profit of 10%-20% which will be project dependent.</p>
      <p>This growth is fueled by the increasing demand for unique property investments in New Zealand and our ability to deliver high-quality services to the market in a condensed time frame, with heavily controlled costs.</p>
      <p>With a solid business model and a dedicated team, we are confident in our ability to achieve success and establish Tarrow Dwellings Investments as a trusted name in the industry.</p>
      <p>New Zealand's property market has been experiencing steady growth over the years, making it an attractive destination for property investors. With its beautiful landscapes and strong economy, New Zealand offers a diverse range of investment opportunities for both local and international investors. The demand for quality properties in prime locations continues to rise, creating a favorable environment for property investment companies like ours that can lean on our modular benefits of being able to reach unique and remote locations.</p>
    </div>
    <div class="photo" role="img" aria-label="Photo of a timber deck with white stone seats behind glass, overlooking green pasture" style="left:24px;top:410px;width:300px;height:67px;background:linear-gradient(180deg,#7f8a5c 0%,#9aa36e 45%,#d8d4cc 65%,#b59a78 100%)"></div>
  </section>

</main>
</body>
</html>
```